Grafik für Software-Entwicklungsunternehmen gesucht
Zielgruppe
Stonmere ist ein Software-Entwicklungsunternehmen, welches die Applikation KOV7Site für Ihre Kunden betreibt und weiter entwickelt. Die Software arbeitet mit KI und augmendet reality uns ist technologisch führend. Alle weiteren Informationen in der PPT.
Aufgabenstellung
Wir brauchen in der Powerpoint-Präsentation eine super coole Grafik, welche die Hauptfunktionalitäten respektive der Prozess zeigt. Die Grafik muss in 3 Prozess-Schritten animiert werden können. Die Datei 'Prozessgrafik' muss als Grafik erstellt werden. Sollte das Budget für animierte Darstellung nicht ausreichen dann bitte melde. Evtl. führen wir den Auftrag dann weiter (Webseite/Kundenpräsentation)

```html
<!DOCTYPE html>
<html lang="de">
<head>
<meta charset="utf-8">
<title>Prozess – Stonmere</title>
<link href="https://fonts.googleapis.com/css2?family=Arimo:wght@400;700&display=swap" rel="stylesheet">
<style>
  :root {
    --bg-deep: #020b0c;
    --bg-teal: #0c3f42;
    --step1: #19c3c7;
    --step1-light: #63d5d6;
    --step2: #15a7a8;
    --step2-light: #60bcbc;
    --step3: #127d7e;
    --step3-light: #6aa5a5;
    --band: #ffffff;
    --text-light: #ffffff;
  }
  * { margin: 0; padding: 0; box-sizing: border-box; }
  html, body { width: 1200px; height: 675px; overflow: hidden; background: var(--bg-deep); }
  body { font-family: "Arimo", Arial, sans-serif; }
  .slide { position: relative; width: 1200px; height: 675px; overflow: hidden; }
  .backdrop {
    position: absolute; inset: 0;
    background:
      radial-gradient(ellipse 55% 35% at 85% 30%, rgba(40,190,190,.55), transparent 70%),
      radial-gradient(ellipse 50% 18% at 45% 40%, rgba(30,160,165,.35), transparent 70%),
      radial-gradient(ellipse 30% 12% at 5% 20%, rgba(40,180,180,.35), transparent 70%),
      linear-gradient(180deg, #041416 0%, var(--bg-teal) 45%, #031011 100%);
  }
  .title {
    position: absolute; left: 52px; top: 46px;
    font-size: 38px; font-weight: 700; color: var(--text-light);
  }
  .process-graphic { position: absolute; inset: 0; }
  .step-number, .step-label, .feature-list, .product-name {
    position: absolute; transform: translateX(-50%); text-align: center; white-space: nowrap;
  }
  .step-number { top: 254px; font-size: 28px; font-weight: 700; }
  .step-label { top: 334px; font-size: 22px; font-weight: 700; }
  .step-1 { color: var(--step1); }
  .step-2 { color: var(--step2); }
  .step-3 { color: var(--step3); }
  .feature-list {
    list-style: none; color: var(--text-light);
    font-size: 12.5px; font-weight: 700; line-height: 18.8px;
  }
  .product-name {
    top: 378px; color: var(--text-light);
    font-size: 39px; font-weight: 700; letter-spacing: -0.5px; line-height: 1;
  }
  .brand {
    position: absolute; left: 46px; top: 606px;
    display: flex; align-items: center; gap: 8px;
    color: var(--text-light); font-size: 20px; font-weight: 400;
  }
  .brand-square { width: 14px; height: 14px; background: var(--text-light); }
</style>
</head>
<body>
<div class="slide">
  <div class="backdrop" role="img" aria-label="Dunkler Hintergrund mit türkis leuchtender digitaler Partikelwelle und Netzwerkpunkten"></div>

  <h1 class="title">Prozess</h1>

  <svg class="process-graphic" width="1200" height="675" viewBox="0 0 1200 675" aria-hidden="true">
    <defs>
      <clipPath id="above-band"><rect x="0" y="0" width="1200" height="316"/></clipPath>
      <clipPath id="below-band"><rect x="0" y="382" width="1200" height="300"/></clipPath>
    </defs>

    <!-- Schritt 1 -->
    <g clip-path="url(#above-band)">
      <polygon points="254,144 454,344 254,544 54,344" fill="var(--step1)" opacity=".25"/>
      <polygon points="254,176 422,344 254,512 86,344" fill="var(--step1)"/>
      <polygon points="254,211 387,344 254,477 121,344" fill="var(--step1-light)"/>
      <polygon points="254,239 359,344 254,449 149,344" fill="#fff"/>
    </g>
    <g clip-path="url(#below-band)">
      <polygon points="254,144 454,344 254,544 54,344" fill="var(--step1)" opacity=".12"/>
      <polygon points="254,176 422,344 254,512 86,344" fill="#128a8c" opacity=".6"/>
      <polygon points="254,239 359,344 254,449 149,344" fill="#9a9a9a" opacity=".6"/>
    </g>

    <!-- Schritt 2 -->
    <g clip-path="url(#above-band)">
      <polygon points="584,144 784,344 584,544 384,344" fill="var(--step2)" opacity=".25"/>
      <polygon points="584,176 752,344 584,512 416,344" fill="var(--step2)"/>
      <polygon points="584,211 717,344 584,477 451,344" fill="var(--step2-light)"/>
      <polygon points="584,239 689,344 584,449 479,344" fill="#fff"/>
    </g>
    <g clip-path="url(#below-band)">
      <polygon points="584,144 784,344 584,544 384,344" fill="var(--step2)" opacity=".12"/>
      <polygon points="584,176 752,344 584,512 416,344" fill="#0f7a7b" opacity=".6"/>
      <polygon points="584,239 689,344 584,449 479,344" fill="#9a9a9a" opacity=".6"/>
    </g>

    <!-- Schritt 3 -->
    <g clip-path="url(#above-band)">
      <polygon points="927,144 1127,344 927,544 727,344" fill="var(--step3)" opacity=".3"/>
      <polygon points="927,176 1095,344 927,512 759,344" fill="var(--step3)"/>
      <polygon points="927,211 1060,344 927,477 794,344" fill="var(--step3-light)"/>
      <polygon points="927,239 1032,344 927,449 822,344" fill="#fff"/>
    </g>
    <g clip-path="url(#below-band)">
      <polygon points="927,144 1127,344 927,544 727,344" fill="var(--step3)" opacity=".15"/>
      <polygon points="927,176 1095,344 927,512 759,344" fill="#0d6667" opacity=".6"/>
      <polygon points="927,239 1032,344 927,449 822,344" fill="#8a9a9a" opacity=".55"/>
    </g>

    <!-- Band -->
    <rect x="0" y="316" width="1200" height="66" fill="var(--band)"/>

    <!-- Pfeile -->
    <polygon points="408,331 437,348 408,365" fill="var(--step1)"/>
    <polygon points="746,331 775,348 746,365" fill="var(--step2)"/>
  </svg>

  <div class="step-number step-1" style="left:255px">01</div>
  <div class="step-number step-2" style="left:585px">02</div>
  <div class="step-number step-3" style="left:927px">03</div>

  <div class="step-label step-1" style="left:252px">PLANUNG</div>
  <div class="step-label step-2" style="left:582px">AUSFÜHRUNG</div>
  <div class="step-label step-3" style="left:944px">LIFECYCLE-MANAGEMENT</div>

  <ul class="feature-list" style="left:256px; top:398px">
    <li>Projekterfassung und Milestones</li>
    <li>Schnittstellen-Management</li>
    <li>BIM-Viewer</li>
  </ul>

  <div class="product-name" style="left:586px">KOV7Site</div>
  <ul class="feature-list" style="left:586px; top:419px">
    <li>Intelligentes Baumanagement</li>
    <li>Augmented reality</li>
    <li>Künstlichen Intelligenz bei…</li>
  </ul>

  <ul class="feature-list" style="left:935px; top:393px">
    <li>Facility-Management</li>
    <li>Objekt-Abnahme</li>
    <li>Garantieleistungen</li>
    <li>Mängelbehebung</li>
    <li>«Digitalisierung» Projekt-Owner</li>
  </ul>

  <div class="brand"><span class="brand-square"></span><span>Stonmere</span></div>
</div>
</body>
</html>
```